Grand Opening Banner needed for Marvelous Floors and Home

My website is www.MarvelousFloorsandHome.example (login with password 'plorvak')

A full page banner 1000px X 500px with bright, lively colors and wording that shows an exciting GRAND OPENING celebration throughout the site. Banner needs to convey the following...

Grand Opening Sale
Runs through end of the month
Savings in every department
30 day Returns
Free Rug Pads with every rug
Free shipping.

Banner can be a simple background with graphics and text, or can be a room scene with rugs and furniture, or a grouping of rugs with text.

Some Ideas and Images can be taken from our vendor's websites, such as:

http://tvsupplyhub.example/
http://borvane.example/borvane_2015/
http://www.pxweaves.example/
http://tassiru.example/
http://shopvelmira.example/

I also have quite a few room scene images available for use, if you desire.

Target Market(s)

Affluent women who care about stylish decor for their homes

Industry/Entity Type

Home And Garden

Requirements
Must have
• bold, vibrant appearance. Text that can be modified in Photoshop.
Nice to have
• HAND DRAWN, ARTIST STYLE ARTWORK IS GREATLY APPRECIATED.
• flat graphics and text with little to no 3 dimensional (shadow) effect. Font styles should be elegant/luxurious. An organic, scribbled, or painted style is nice in keeping with the handmade products that we sell.
• I am open to changing the color scheme of the website, to match your banner, so don't feel tied down to my existing colors.
Should not have
• nothing too modern or extreme in style.

```html
<!DOCTYPE html>
<html lang="en">
<head>
<meta charset="utf-8">
<title>Grand Opening Sale Banner</title>
<link rel="stylesheet" href="https://fonts.googleapis.com/css2?family=Cinzel:wght@600&family=Tenor+Sans&family=Open+Sans:wght@400&display=swap">
<style>
  :root {
    --page-bg: #ffffff;
    --headline-yellow: #f7ec17;
    --list-white: #f4f2ee;
    --sale-red: #a0141b;
    --sale-text: #ffffff;
    --room-mid: #6b5a4d;
    --room-light: #b9afa3;
    --floor-brown: #2e1d15;
  }
  * { margin: 0; padding: 0; box-sizing: border-box; }
  html, body {
    width: 1200px;
    height: 1200px;
    overflow: hidden;
    background: var(--page-bg);
  }
  .canvas {
    position: relative;
    width: 1200px;
    height: 1200px;
    background: var(--page-bg);
  }
  .banner {
    position: absolute;
    top: 0;
    left: 0;
    width: 1200px;
    height: 600px;
    overflow: hidden;
  }
  .room-scene {
    position: absolute;
    inset: 0;
    background:
      radial-gradient(ellipse 320px 140px at 620px 470px, rgba(92,28,24,0.85), rgba(92,28,24,0) 70%),
      radial-gradient(ellipse 260px 200px at 700px 160px, rgba(215,210,205,0.7), rgba(215,210,205,0) 70%),
      radial-gradient(ellipse 160px 200px at 1080px 200px, rgba(60,50,40,0.6), rgba(60,50,40,0) 70%),
      linear-gradient(180deg, var(--room-light) 0%, var(--room-mid) 45%, #4a3a30 72%, var(--floor-brown) 100%);
  }
  .left-shade {
    position: absolute;
    top: 0;
    left: 0;
    width: 420px;
    height: 600px;
    background: linear-gradient(90deg, #050505 0%, rgba(20,18,16,0.85) 35%, rgba(40,35,30,0.35) 75%, rgba(40,35,30,0) 100%);
  }
  .perks {
    position: absolute;
    left: 51px;
    top: 236px;
    list-style: none;
    font-family: "Tenor Sans", "Optima", sans-serif;
    font-size: 20px;
    color: var(--list-white);
    letter-spacing: 0.2px;
  }
  .perks li { position: absolute; left: 0; white-space: nowrap; }
  .perks li:nth-child(1) { top: 0; }
  .perks li:nth-child(2) { top: 61px; }
  .perks li:nth-child(3) { top: 122px; }
  .perks li:nth-child(4) { top: 178px; }
  .perks li:nth-child(5) { top: 238px; }
  .sale-badge {
    position: absolute;
    left: 954px;
    top: 360px;
    width: 218px;
    height: 218px;
  }
  .headline {
    position: absolute;
    left: 458px;
    top: 205px;
    font-family: "Cinzel", "Trajan Pro", serif;
    font-weight: 600;
    color: var(--headline-yellow);
    line-height: 1;
    text-shadow: 1px 2px 3px rgba(0,0,0,0.35);
  }
  .headline-line {
    display: block;
    font-size: 146px;
    white-space: nowrap;
  }
  .headline-line.grand { letter-spacing: 16px; }
  .headline-line.opening { letter-spacing: -2px; }
  .headline .small-caps { font-size: 106px; }
  .sale-word {
    position: absolute;
    left: 954px;
    top: 360px;
    width: 218px;
    height: 218px;
    overflow: visible;
  }
</style>
</head>
<body>
  <main class="canvas">
    <section class="banner">
      <div class="room-scene" role="img" aria-label="Living room scene with a patterned red area rug, dark sofa, armchairs, fireplace, chandelier and framed artwork on the walls"></div>
      <div class="left-shade"></div>

      <ul class="perks">
        <li>Runs through end of the month</li>
        <li>Free rug pads with every rug</li>
        <li>Savings in every department</li>
        <li>30 day returns</li>
        <li>Free shipping</li>
      </ul>

      <svg class="sale-badge" viewBox="0 0 218 218" aria-hidden="true">
        <circle cx="109" cy="109" r="109" fill="var(--sale-red)" opacity="0.92"/>
      </svg>

      <h1 class="headline">
        <span class="headline-line grand">G<span class="small-caps">RAND</span></span>
        <span class="headline-line opening">O<span class="small-caps">PENING</span></span>
      </h1>

      <svg class="sale-word" viewBox="0 0 218 218">
        <text x="104" y="148" text-anchor="middle" transform="rotate(-22 104 128)"
              font-family="'Open Sans', sans-serif" font-size="76" fill="var(--sale-text)">sale</text>
      </svg>
    </section>
  </main>
</body>
</html>
```